Velmoxa AdAgency Presentation

We need ppt design for an ad agency re-branding, agency is based in Moscow, Russia. Our specifics is brand audit, consulting and strategy in web and offline.
We decided to do re-branding because our current agency does not answer the purpose and we need a kind of "second breath".
The idea of re-branding appeared because of many changes that happened in company: new clients, new projects level, new team.
So we'd like to promote company of changes and design should show this spirit as possible.
You may use info in attached pdf file (sorry for Russian language). Info is not so necessary, it will be replaced later.

Please use more colors than digital blue and grey!

Industry/Entity Type

Ad Agency

Requirements
Must have
• Logo is attached. Please choose one.

Ppt project should include:
- Front and last page design
- Heading and list design
- Page-separator design
- Diagram design
- Pics appearance

```html
<!DOCTYPE html>
<html lang="en">
<head>
<meta charset="utf-8">
<title>Velmoxa — Say Hello to Our Team</title>
<link href="https://fonts.googleapis.com/css2?family=Questrial&family=Mulish:wght@700;800&family=PT+Sans:wght@400;700&display=swap" rel="stylesheet">
<style>
  :root {
    --bg-top: #ecebe0;
    --bg-bottom: #f8f8f2;
    --ink: #3a3a3a;
    --ink-soft: #4a4a4a;
    --accent: #1ba3dd;
    --accent-coral: #f26b4f;
    --accent-lime: #8cc63f;
    --accent-amber: #f6b426;
    --accent-berry: #c2408f;
    --divider: #dcdcd2;
    --footer: #303133;
    --footer-dark: #242527;
    --white: #ffffff;
    --photo-a: #9fb3bd;
    --photo-b: #c9d3d6;
    --photo-c: #5d6a74;
  }
  * { margin: 0; padding: 0; box-sizing: border-box; }
  html, body { width: 1200px; height: 900px; overflow: hidden; }
  body {
    position: relative;
    background: linear-gradient(180deg, var(--bg-top) 0%, var(--bg-bottom) 75%);
    font-family: "Questrial", sans-serif;
    color: var(--ink);
  }
  .site-url {
    position: absolute; right: 64px; top: 34px;
    white-space: nowrap;
    font-size: 19px; letter-spacing: 0.4px; color: var(--ink);
  }
  .site-url span { color: var(--accent); }
  .title {
    position: absolute; left: 63px; top: 46px;
    font-weight: 400; line-height: 1;
  }
  .title .line-1 { display: block; font-size: 80px; letter-spacing: 0.5px; color: var(--ink); }
  .title .line-2 { display: block; font-size: 62px; color: var(--accent); margin-top: 6px; letter-spacing: 0.5px; }
  .tagline {
    position: absolute; left: 65px; top: 209px;
    font-family: "Mulish", sans-serif; font-weight: 800;
    font-size: 27px; color: var(--ink-soft); letter-spacing: -0.3px;
  }
  .divider {
    position: absolute; top: 280px; width: 1px; height: 393px;
    background: var(--divider);
  }
  .team-card { position: absolute; width: 316px; }
  .team-photo {
    width: 316px; height: 127px;
    background: linear-gradient(160deg, var(--photo-b) 0%, var(--photo-a) 45%, var(--photo-c) 100%);
    border-bottom: 4px solid var(--card-accent);
  }
  .team-card.coral { --card-accent: var(--accent-coral); }
  .team-card.lime { --card-accent: var(--accent-lime); }
  .team-card.amber { --card-accent: var(--accent-amber); }
  .member-name {
    margin: 27px 0 0 5px;
    font-family: "Mulish", sans-serif; font-weight: 800;
    font-size: 23px; color: var(--ink-soft);
  }
  .member-bio {
    margin-top: 10px; width: 307px;
    font-size: 16px; line-height: 22px; letter-spacing: 0.45px;
    text-align: justify; color: var(--ink-soft);
  }
  .member-bio + .member-bio { margin-top: 26px; }
  .footer {
    position: absolute; left: 0; top: 780px; width: 1200px; height: 97px;
    background: radial-gradient(ellipse at 20% 50%, var(--footer-dark) 0%, var(--footer) 40%);
  }
  .footer-band {
    position: absolute; left: 0; top: 877px; width: 1200px; height: 23px;
    background: linear-gradient(90deg,
      var(--accent) 0 40%,
      var(--accent-coral) 40% 60%,
      var(--accent-amber) 60% 75%,
      var(--accent-lime) 75% 90%,
      var(--accent-berry) 90% 100%);
  }
  .brand {
    position: absolute; left: 60px; top: 812px;
    display: flex; align-items: center; gap: 10px;
    font-family: "PT Sans", sans-serif; font-size: 22px; color: #c9c9c9;
  }
  .brand-mark { width: 16px; height: 16px; background: var(--accent-coral); }
  .pager {
    position: absolute; left: 516px; top: 811px;
    display: flex; align-items: center; gap: 8px;
    font-family: "PT Sans", sans-serif;
  }
  .pager-btn { width: 28px; height: 28px; display: block; }
  .pager-box {
    width: 42px; height: 36px; border-radius: 5px;
    background: #1c1d1f; box-shadow: inset 0 1px 3px rgba(0,0,0,0.7);
    display: flex; align-items: center; justify-content: center;
    font-size: 18px;
  }
  .pager-box.current { color: var(--accent); }
  .pager-box.total { color: #b8b8b8; }
  .pager-of { font-style: italic; font-weight: 700; font-size: 18px; color: #9a9a9a; }
  .contact {
    position: absolute; left: 895px; top: 811px;
    font-family: "PT Sans", sans-serif; white-space: nowrap;
  }
  .contact-label { font-size: 14px; color: var(--accent); }
  .contact-address { font-size: 14px; font-weight: 700; color: var(--white); margin-top: 1px; }
</style>
</head>
<body>
  <div class="site-url">www.<span>velmoxa-agency</span>.com</div>

  <h1 class="title">
    <span class="line-1">SAY HELLO TO</span>
    <span class="line-2">OUR TEAM</span>
  </h1>
  <p class="tagline">Meet the amazing folks!</p>

  <div class="divider" style="left:413px"></div>
  <div class="divider" style="left:799px"></div>

  <section class="team-card coral" style="left:61px; top:289px">
    <div class="team-photo" role="img" aria-label="Group photo of the agency team in a bright office"></div>
    <h2 class="member-name">Team Member</h2>
    <p class="member-bio">Lorem Ipsum is simply dummy text of the printing and typesetting.</p>
    <p class="member-bio">Lorem Ipsum has been the industry's standard dummy text ever since the 1500s, when an unknown printer took a galley of type and scrambled it to make a type specimen book.</p>
  </section>

  <section class="team-card lime" style="left:449px; top:289px">
    <div class="team-photo" role="img" aria-label="Group photo of the agency team in a bright office"></div>
    <h2 class="member-name">Team Member</h2>
    <p class="member-bio">Lorem Ipsum is simply dummy text of the printing and typesetting.</p>
    <p class="member-bio">Lorem Ipsum has been the industry's standard dummy text ever since the 1500s, when an unknown printer took a galley of type and scrambled it to make a type specimen book.</p>
  </section>

  <section class="team-card amber" style="left:828px; top:299px">
    <div class="team-photo" role="img" aria-label="Group photo of the agency team in a bright office"></div>
    <h2 class="member-name" style="margin-top:17px">Team Member</h2>
    <p class="member-bio">Lorem Ipsum is simply dummy text of the printing and typesetting.</p>
    <p class="member-bio">Lorem Ipsum has been the industry's standard dummy text ever since the 1500s, when an unknown printer took a galley of type and scrambled it to make a type specimen book.</p>
  </section>

  <footer>
    <div class="footer"></div>
    <div class="footer-band"></div>

    <div class="brand"><span class="brand-mark"></span>Velmoxa</div>

    <nav class="pager" aria-label="Slide navigation">
      <svg class="pager-btn" viewBox="0 0 28 28" aria-label="Previous slide">
        <circle cx="14" cy="14" r="13" fill="#1ba3dd"/>
        <path d="M16 8.5 L10.5 14 L16 19.5" fill="none" stroke="#ffffff" stroke-width="3" stroke-linecap="round" stroke-linejoin="round"/>
      </svg>
      <span class="pager-box current">3</span>
      <span class="pager-of">of</span>
      <span class="pager-box total">6</span>
      <svg class="pager-btn" viewBox="0 0 28 28" aria-label="Next slide">
        <circle cx="14" cy="14" r="13" fill="#1ba3dd"/>
        <path d="M12 8.5 L17.5 14 L12 19.5" fill="none" stroke="#ffffff" stroke-width="3" stroke-linecap="round" stroke-linejoin="round"/>
      </svg>
    </nav>

    <div class="contact">
      <div class="contact-label">Contact Us</div>
      <div class="contact-address">The Company address looks good in footer</div>
    </div>
  </footer>
</body>
</html>
```